Carte d'affaire bilingue

Nous avons besoin d'une carte d'affaire pour notre entreprise spécialisée en vente et achat de terrain. Nous sommes une agence immobilière et nous voulons une carte avec le recto en Français et le verso en anglais. Nous voulons une image sobre et épurée. Nous avons de la clientèle internationale et nous voulons une carte très professionnelle mais qui se démarque. Nous voulons cibler une clientèle commerciale, industrielle, contracteurs et promoteurs immobiliers.
Updates

Hi everybody, we saw all your conception and we are approching of what we like but the "WOW" is missing.

We love the little sign to specify (phone or email) but we can put them in a square to make like our logo, we love also dark gray not lite gray, we also love the stainless lines. In our logo you can see a little sign +. For us is signyfy " Always further" so if you can put many little +++++ in the conception somewhere very discret it will be appreciate. We also like a kind of round that make a magnyfying glass, because we search land we found opportunity.

Thank you

Reason: I ask different things in the last day but no one do what i am asking for. For the conception # 3016702 that we love we ask changes.

We like simplicity, urban design, corporate, international. The card must have one side in french and the other side in english. We like dark gray,silver, and a little bit of green.

Target Market(s)

Investors, developers, construction builders, etc...

Font styles to use
Serif
Sans Serif

Requirements
Must have
• logo
La mention: Agence immobilière (Francais) / Real Estate Agency (anglais)
Sous le nom: Courtier immobilier agréé (Français) / Real Estate Broker

```html
<!DOCTYPE html>
<html lang="fr">
<head>
<meta charset="utf-8">
<title>Carte d'affaires bilingue</title>
<link rel="stylesheet" href="https://fonts.googleapis.com/css2?family=Lato:wght@400;700&display=swap">
<style>
  :root {
    --backdrop: #d9d9d9;
    --card: #ffffff;
    --green: #138f45;
    --grey: #6d6e70;
    --on-green: #ffffff;
  }
  * { margin: 0; padding: 0; box-sizing: border-box; }
  html, body {
    width: 1200px;
    height: 750px;
    overflow: hidden;
    background: var(--backdrop);
    font-family: "Lato", sans-serif;
  }
  .canvas {
    width: 1200px;
    height: 750px;
    display: flex;
    flex-direction: column;
    align-items: center;
    justify-content: center;
    gap: 44px;
  }
  .card {
    position: relative;
    width: 560px;
    height: 310px;
    background: var(--card);
    border-radius: 26px;
    overflow: hidden;
  }
  .contact-panel {
    position: absolute;
    top: 0;
    right: 0;
    width: 308px;
    height: 262px;
    background: var(--green);
    color: var(--on-green);
    padding: 66px 24px 0 30px;
    font-size: 14px;
    line-height: 1.32;
  }
  .contact-panel .address { margin-bottom: 18px; }
  .identity {
    position: absolute;
    left: 34px;
    top: 148px;
    width: 210px;
  }
  .brand {
    display: flex;
    align-items: center;
    gap: 8px;
    margin-bottom: 10px;
  }
  .brand-mark {
    width: 22px;
    height: 22px;
    background: var(--green);
    flex: none;
  }
  .brand-name {
    font-size: 17px;
    font-weight: 700;
    color: var(--grey);
    letter-spacing: 0.02em;
    white-space: nowrap;
  }
  .role {
    color: var(--green);
    font-weight: 700;
    font-size: 17px;
    line-height: 1.2;
  }
  .role.secondary { font-size: 15px; }
</style>
</head>
<body>
<main class="canvas">

  <section class="card card-fr" lang="fr">
    <div class="identity">
      <div class="brand">
        <span class="brand-mark"></span>
        <span class="brand-name">Le Repère Foncier</span>
      </div>
      <p class="role">Agence immobilière</p>
      <p class="role secondary">Courtier immobilier agréé</p>
    </div>
    <div class="contact-panel">
      <p class="address">Adresse: 12 B boul. des Artisans, 3e<br>Mirabel, Qc, J7N 1A4</p>
      <p>email: m.tremblay@lrfoncier.com<br>
         web site: www.lrfoncier.com<br>
         phone number: 514-555-0182<br>
         fax: 450-555-0147<br>
         toll free: 1-866-555-0100</p>
    </div>
  </section>

  <section class="card card-en" lang="en">
    <div class="identity">
      <div class="brand">
        <span class="brand-mark"></span>
        <span class="brand-name">Land Marker</span>
      </div>
      <p class="role">Real Estate Agency</p>
      <p class="role secondary">Real Estate Broker</p>
    </div>
    <div class="contact-panel">
      <p class="address">Adresse: 12 B boul. des Artisans, 3e<br>Mirabel, Qc, J7N 1A4</p>
      <p>email: m.tremblay@lrfoncier.com<br>
         web site: www.lrfoncier.com<br>
         phone number: 514-555-0182<br>
         fax: 450-555-0147<br>
         toll free: 1-866-555-0100</p>
    </div>
  </section>

</main>
</body>
</html>
```